WordPress design for BraxtonVell.com

*****
OVERVIEW
*****
BraxtonVell.com needs a fresh, clean, professional design that effectively illustrates its talent in a thoughtful, impressive, and impactful way.
Vell Architecture & Interiors (www.braxtonvell.com) is a well-established, prestigious, well-publicized New England USA architecture firm. Founded in 1996, the privately-held company specializes in high-end residential projects with a focus on classic New England style architecture.
Business contact information is as noted below:
Address:
Vell Architecture & Interiors
87 Orchard Terrace
Needham, MA 02817
Telephone:
617-555-0138
781-555-0274
Email:
info@braxtonvell.com
An excerpt from the current site describes the outfit with this:
"Our architecture and interior design practices are centered around the philosophy that successful living spaces combine a focus on richly articulated detail and an in-depth knowledge of quality construction techniques."
*****
DESIGN RESEARCH
*****
In reviewing design ideas, the following sites were appealing:
Good
- Marcus Thorne Architects (http://mtaarchitects-example.com/) - Simple and clean, but almost too simple.
Better
- Penrose Galt Architecture (http://www.penrosegalt-example.com/) - Direct portfolio access. Simple and clean.
Best
- Brimwell Architects (http://www.brimwellarchitects-example.com/) - Clean, simple, easy to navigate
- QRV Architecture & Interiors (http://www.qrv-architects-example.com/) - Excellent use of high-resolution media, transitions, and navigation.
Here is an example of what is NOT desired:
Tolland Pryce Architects (http://www.tollandpryce-example.com/) - Cluttered, tight landing page. Uncertain navigation.
*****
OTHER DETAILS
*****
The grey in the Vell Architecture & Interiors logo is hex 636363. The font is unknown.
Updates
Project Deadline Extended
Reason: Hello everyone,
Thank you for your continued patience with this project. As it turns out, a critical member of the decision making team on our client's end has been out of the office this week. She will be back next week and is ready to be fully engaged with this. That said, we are extending the contest for at least 5 days. Next week will be much more active.
Thank you for your understanding.
Glasswick Technology Services
Project Deadline Extended
Reason: Hello everyone,
The customer was on vacation and only returned Monday of this week. That said, we need to extend the deadline for 5 days to afford time for review and comment.
Thank you for your patience! The designs submitted thus far are fantastic!
Thanks again,
Project Deadline Extended
Reason: Hello,
With so many designs, the customer is taking longer than anticipated to review them. They are looking at them offline and will process a large batch of comments when ready.
That said, the contest is being extended again.
Thank you for your continued patience.
Project Deadline Extended
Reason: Hello,
Because there are 108 designs to review and comment on, this is taking much longer than anticipated. That said, the contest is being extended another 5 days to ensure the customer has the desired outcome.
Thank you,
Target Market(s)
- Would-be clients
- Landowners
- Construction firms and general contractors
- High-end residential component manufacturers
- Media outlets
- All others interested in high-end residential architecture and interior design
Industry/Entity Type
Architecture
Requirements
Must have
- - Lots of media capabilities, such as embedded video (via ClipStream is fine), project image gallery, sliders for various functions, and social media integrations
- - At least one large slider on the landing page is critical, as well as space for standard lead-in things, such as news/events, opportunities, project highlights, and the likes
- - A high-resolution project showcase - finished projects and works in progress - is critical
- - A place to highlight business partners with the potential for reciprocation
- Form capabilities for things like information requests and general contacts from the public
- - Design must be handed off in a logically-layered (for WordPress) PSD with any and all additional source files provided (e.g. Photoshop, Illustrator, fonts, etc)
Nice to have
- - The WordPress design should be capable of fitting into the very popular FernLayouts Trellis theme.

```html
<!DOCTYPE html>
<html lang="en">
<head>
<meta charset="utf-8">
<title>Vell Architecture &amp; Interiors</title>
<link rel="stylesheet" href="https://fonts.googleapis.com/css2?family=Montserrat:wght@500;600;700&family=Open+Sans:wght@400;600;700&display=swap">
<style>
:root{
  --brand-grey:#636363;
  --ink:#3d3d3d;
  --muted:#8a8a8a;
  --line:#d9d9d9;
  --portfolio-bg:#e4ecf0;
  --testimonial-bg:#efefef;
  --footer-bg:#f3f3f3;
  --button:#555555;
  --partner:#6a6a6a;
  --accent:#e08a2e;
  --dot:#8c8c8c;
  --white:#ffffff;
}
*{box-sizing:border-box;margin:0;padding:0}
html,body{width:1200px;height:3348px;overflow:hidden;background:var(--white)}
body{font-family:"Open Sans",Arial,sans-serif;color:var(--ink);position:relative}
.wrap{width:1136px;margin:0 auto}

/* top bar */
.topbar{height:48px;display:flex;align-items:center;gap:18px;padding-left:32px;border-bottom:1px solid #eee}
.topbar .social{width:18px;height:18px;border-radius:50%;background:#9a9a9a}

/* masthead wordmark: plain text in the site font */
.masthead{height:200px;display:flex;flex-direction:column;align-items:center;justify-content:center}
.brand-name,.brand-sub{font-family:"Montserrat",sans-serif;font-weight:500;color:var(--brand-grey);white-space:nowrap;text-transform:uppercase}
.brand-name{font-size:64px;letter-spacing:8px;line-height:1}
.brand-sub{font-size:18px;letter-spacing:3px;margin-top:10px}

/* navigation */
.main-nav{height:56px;border-top:1px solid var(--line);border-bottom:1px solid var(--line);display:flex;align-items:center;justify-content:space-between;padding:0 32px}
.main-nav a{font-family:"Montserrat",sans-serif;font-size:12px;font-weight:600;color:var(--ink);text-decoration:none;letter-spacing:.4px;white-space:nowrap}
.main-nav a.current{border-bottom:2px solid var(--ink);padding-bottom:4px}

/* hero */
.hero{position:relative;height:408px;margin-top:8px;background:linear-gradient(180deg,#cfe0ee 0%,#b9c8d4 35%,#8e989e 62%,#6f8a5a 82%,#4f6b3a 100%)}
.hero .arrow{position:absolute;top:190px;width:24px;height:24px;fill:none;stroke:#fff;stroke-width:3}
.hero .prev{left:14px}.hero .next{right:14px}

/* section titles */
.section-title{font-family:"Montserrat",sans-serif;font-weight:600;font-size:40px;letter-spacing:2px;color:var(--ink);text-align:center;text-transform:uppercase}

/* about */
.about{display:flex;gap:34px;padding:52px 32px 0;height:420px}
.video{position:relative;width:520px;height:332px;background:#050505;flex:none}
.video .controls{position:absolute;left:0;right:0;bottom:0;height:44px;background:#1b1b1b;display:flex;align-items:center;gap:14px;padding:0 14px}
.video .play{width:0;height:0;border-left:14px solid #fff;border-top:9px solid transparent;border-bottom:9px solid transparent}
.video .track{flex:1;height:8px;background:#4a4a4a;position:relative}
.video .track span{position:absolute;left:0;top:0;bottom:0;width:62%;background:#3c8ed8}
.video .ctl{width:16px;height:14px;border:2px solid #fff}
.about-text h2{font-family:"Montserrat",sans-serif;font-weight:600;font-size:40px;letter-spacing:2px;line-height:1;margin-bottom:22px}
.about-text p{font-size:14px;line-height:1.55;color:var(--muted);margin-bottom:14px}
.about-text .more{font-size:16px;font-weight:700;color:var(--ink)}

/* portfolio */
.portfolio{background:var(--portfolio-bg);height:808px;padding-top:52px}
.tabs{display:flex;justify-content:center;gap:18px;margin-top:20px;font-family:"Montserrat",sans-serif;font-size:16px;font-weight:500;letter-spacing:1px;color:var(--ink)}
.tabs .current{border-bottom:2px solid var(--ink)}
.tabs .sep{color:var(--muted)}
.grid{display:grid;grid-template-columns:repeat(4,266px);column-gap:24px;row-gap:20px;margin-top:62px}
.tile-img{position:relative;height:188px}
.grid .row2 .tile-img{height:160px}
.tile-label{font-family:"Montserrat",sans-serif;font-size:17px;font-weight:600;letter-spacing:1px;text-align:center;margin-top:18px}
.overlay{position:absolute;inset:0;background:rgba(60,60,60,.55);display:flex;align-items:center;justify-content:center;font-family:"Montserrat",sans-serif;color:#fff;font-size:22px;font-weight:600;letter-spacing:1px}
.btn{display:block;width:168px;margin:38px auto 0;background:var(--button);color:#fff;text-align:center;font-family:"Montserrat",sans-serif;font-weight:600;font-size:18px;letter-spacing:1px;padding:10px 0}
.warm1{background:linear-gradient(135deg,#6b3a24,#b98a5a)}
.warm2{background:linear-gradient(135deg,#a8845a,#e6d2b0)}
.warm3{background:linear-gradient(135deg,#7a4a2a,#c9a070)}
.warm4{background:linear-gradient(135deg,#5a2f1c,#d8b080)}
.cool1{background:linear-gradient(135deg,#7d7d7d,#d9d3c8)}
.cool2{background:linear-gradient(135deg,#8a7a66,#efe7da)}

/* publications */
.publications{position:relative;height:384px;padding-top:60px}
.pubs{display:grid;grid-template-columns:repeat(4,250px);justify-content:space-between;width:1060px;margin:48px auto 0}
.pub-img{position:relative;height:140px;background:linear-gradient(135deg,#d8d2c6,#f7f4ef);border:1px solid #ddd}
.pub-label{font-family:"Montserrat",sans-serif;font-size:15px;font-weight:600;letter-spacing:.5px;text-align:center;margin-top:24px;white-space:nowrap}
.pub-arrow{position:absolute;top:212px;width:26px;height:40px;fill:var(--ink)}
.pub-arrow.left{left:4px}.pub-arrow.right{right:4px}

/* testimonials */
.testimonials{background:var(--testimonial-bg);height:388px;padding-top:30px}
.subtitle{text-align:center;font-family:"Montserrat",sans-serif;font-size:15px;letter-spacing:1px;color:var(--muted);margin-top:4px;text-transform:uppercase}
.quotes{display:flex;justify-content:space-between;margin-top:60px;padding:0 40px}
.quote{display:flex;gap:26px;width:520px}
.avatar{width:112px;height:112px;border-radius:50%;flex:none;background:linear-gradient(160deg,#c9c3bb,#5a5552)}
.quote p{font-size:15px;line-height:1.45;color:var(--ink)}
.quote .name{font-family:"Montserrat",sans-serif;color:var(--accent);font-weight:600;font-size:14px;letter-spacing:1px;margin-top:14px;text-transform:uppercase}
.dots{display:flex;justify-content:center;gap:8px;margin-top:34px}
.dots span{width:18px;height:18px;border-radius:50%;background:var(--dot)}
.dots span.on{background:var(--accent)}

/* partners */
.partners{height:240px;padding-top:44px}
.partner-row{display:flex;justify-content:space-between;padding:0 32px;margin-top:44px}
.partner{width:160px;height:60px;background:var(--partner)}

/* footer */
.site-footer{background:var(--footer-bg);height:388px;padding:28px 32px 0;border-top:1px solid var(--line)}
.footer-top{display:flex;gap:40px;align-items:flex-start}
.footer-brand{flex:none;text-align:center}
.footer-brand .brand-name{font-size:52px;letter-spacing:6px}
.footer-brand .brand-sub{font-size:13px;letter-spacing:2px;margin-top:8px}
.footer-about h3{font-family:"Montserrat",sans-serif;font-weight:700;font-size:19px;letter-spacing:1px;text-transform:uppercase;margin:4px 0 10px}
.footer-about p{font-size:14px;line-height:1.55;color:var(--muted)}
.contact-row{display:flex;justify-content:space-between;align-items:center;border-top:1px solid var(--line);border-bottom:1px solid var(--line);margin-top:52px;height:76px;padding:0 160px}
.contact-row span{display:flex;align-items:center;gap:12px;font-size:14px;color:var(--ink)}
.contact-row svg{width:18px;height:18px;fill:var(--muted)}
.legal{margin-top:24px;font-size:13px;line-height:1.7;color:var(--muted)}
</style>
</head>
<body>

<div class="topbar">
  <span class="social"></span><span class="social"></span><span class="social"></span><span class="social"></span><span class="social"></span>
</div>

<header class="masthead">
  <div class="brand-name">Vell</div>
  <div class="brand-sub">Architecture &amp; Interiors</div>
</header>

<nav class="main-nav">
  <a class="current" href="#">HOME</a>
  <a href="#">ABOUT</a>
  <a href="#">ARCHITECTURE</a>
  <a href="#">INTERIOR DESIGN</a>
  <a href="#">WORKS IN PROGRESS</a>
  <a href="#">RENOVATIONS AND ADDITIONS</a>
  <a href="#">RECOGNITION</a>
  <a href="#">AFFILIATES</a>
  <a href="#">CONTACT</a>
</nav>

<section class="hero" role="img" aria-label="Slider photo of a grey-shingled New England residence with white trim and landscaped lawn">
  <svg class="arrow prev" viewBox="0 0 24 24"><path d="M16 3 7 12l9 9"/></svg>
  <svg class="arrow next" viewBox="0 0 24 24"><path d="M8 3l9 9-9 9"/></svg>
</section>

<section class="about">
  <div class="video" role="img" aria-label="Embedded video player showing the firm's introduction film">
    <div class="controls"><span class="play"></span><span class="track"><span></span></span><span class="ctl"></span><span class="ctl"></span></div>
  </div>
  <div class="about-text">
    <h2>ABOUT US</h2>
    <p>Vell Architecture &amp; Interiors is a Boston based firm specializing in architecture and interior design for custom residences. Since our inception in 1996, we have designed homes that reflect our reverence for traditional architecture and our commitment to creating a collaborative working relationship with our clients.</p>
    <p>Our architecture and interior design practices are centered around the philosophy that successful living spaces combine a focus on richly articulated detail and an in-depth knowledge of quality construction techniques.</p>
    <p>The architectural design team is led by Braxton Vell, principal. Braxton's leadership and experience is evident in all aspects of the home design and building process. The interior design team brings equal care, blending classic style with modern comfort for each client and each independent project.</p>
    <span class="more">Read more</span>
  </div>
</section>

<section class="portfolio">
  <h2 class="section-title">PORTFOLIO</h2>
  <div class="tabs">
    <span>ARCHITECTURE</span><span class="sep">/</span>
    <span class="current">INTERIOR DESIGN</span><span class="sep">/</span>
    <span>RENOVATIONS AND ADDITIONS</span><span class="sep">/</span>
    <span>WORKS IN PROGRESS</span>
  </div>
  <div class="wrap grid">
    <div><div class="tile-img warm1" role="img" aria-label="Interior photo of a wood-panelled library"></div><div class="tile-label">BEACON HILL</div></div>
    <div><div class="tile-img warm2" role="img" aria-label="Interior photo of a bright sitting room"></div><div class="tile-label">BEACON STREET</div></div>
    <div><div class="tile-img warm3" role="img" aria-label="Interior photo of a dining room with chandelier"></div><div class="tile-label">MILFORD STREET</div></div>
    <div><div class="tile-img warm4" role="img" aria-label="Interior photo of a warm living room"></div><div class="tile-label">MILFORD STREET</div></div>
    <div class="row2"><div class="tile-img cool1" role="img" aria-label="Interior photo of a stair hall"><div class="overlay">VIEW DETAIL</div></div><div class="tile-label">NEWTON</div></div>
    <div class="row2"><div class="tile-img cool2" role="img" aria-label="Interior photo of a white kitchen"></div><div class="tile-label">NEWTON</div></div>
    <div class="row2"><div class="tile-img warm1" role="img" aria-label="Interior photo of a fireplace sitting area"></div><div class="tile-label">RENDEZVOUS</div></div>
    <div class="row2"><div class="tile-img warm3" role="img" aria-label="Interior photo of a showhouse room"></div><div class="tile-label">SHOWHOUSE</div></div>
  </div>
  <span class="btn">VIEW ALL</span>
</section>

<section class="publications">
  <h2 class="section-title">PUBLICATIONS</h2>
  <svg class="pub-arrow left" viewBox="0 0 26 40"><path d="M26 0 0 20l26 20z"/></svg>
  <svg class="pub-arrow right" viewBox="0 0 26 40"><path d="M0 0l26 20L0 40z"/></svg>
  <div class="pubs">
    <div><div class="pub-img" role="img" aria-label="Magazine feature spread"><div class="overlay">VIEW DETAIL</div></div><div class="pub-label">LEDGER</div></div>
    <div><div class="pub-img" role="img" aria-label="Magazine feature spread"></div><div class="pub-label">HEARTH &amp; YARD</div></div>
    <div><div class="pub-img" role="img" aria-label="Magazine feature spread"></div><div class="pub-label">NORTHEAST DWELLING</div></div>
    <div><div class="pub-img" role="img" aria-label="Magazine feature spread"></div><div class="pub-label">HARBOR COAST MAGAZINES</div></div>
  </div>
</section>

<section class="testimonials">
  <h2 class="section-title">TESTIMONIALS</h2>
  <div class="subtitle">Customers say about us</div>
  <div class="quotes">
    <div class="quote">
      <div class="avatar" role="img" aria-label="Client portrait"></div>
      <div><p>Working with the team was a pleasure from the first sketch to the final walkthrough. Every detail of our home was considered, and the craftsmanship shows in each room we live in today.</p><div class="name">Dorian Pell</div></div>
    </div>
    <div class="quote">
      <div class="avatar" role="img" aria-label="Client portrait"></div>
      <div><p>They listened closely to what our family needed and delivered a classic design that feels warm and timeless. The process was clear, collaborative and always on schedule with our builder.</p><div class="name">Lena Harlow</div></div>
    </div>
  </div>
  <div class="dots"><span></span><span></span><span class="on"></span></div>
</section>

<section class="partners">
  <h2 class="section-title">OUR PARTNERS</h2>
  <div class="partner-row">
    <span class="partner"></span><span class="partner"></span><span class="partner"></span><span class="partner"></span><span class="partner"></span><span class="partner"></span>
  </div>
</section>

<footer class="site-footer">
  <div class="footer-top">
    <div class="footer-brand">
      <div class="brand-name">Vell</div>
      <div class="brand-sub">Architecture &amp; Interiors</div>
    </div>
    <div class="footer-about">
      <h3>Vell Architecture and Interiors</h3>
      <p>Vell Architecture &amp; Interiors is a Boston based firm specializing in architecture and interior design for custom residences. Since our inception in 1996, we have designed homes that reflect our reverence for traditional architecture and our commitment to creating a collaborative working relationship with our clients.</p>
    </div>
  </div>
  <div class="contact-row">
    <span><svg viewBox="0 0 24 24"><path d="M12 2a7 7 0 0 0-7 7c0 5 7 13 7 13s7-8 7-13a7 7 0 0 0-7-7zm0 9.5A2.5 2.5 0 1 1 12 6a2.5 2.5 0 0 1 0 5.5z"/></svg>87 Orchard Terrace Needham, MA 02817</span>
    <span><svg viewBox="0 0 24 24"><path d="M2 5h20v14H2zm2 2v.5l8 5 8-5V7z"/></svg>info@braxtonvell.com</span>
    <span><svg viewBox="0 0 24 24"><path d="M6.6 10.8a15 15 0 0 0 6.6 6.6l2.2-2.2c.3-.3.7-.4 1-.2 1.1.4 2.3.6 3.6.6.6 0 1 .4 1 1V20c0 .6-.4 1-1 1A17 17 0 0 1 3 4c0-.6.4-1 1-1h3.5c.6 0 1 .4 1 1 0 1.3.2 2.5.6 3.6.1.3 0 .7-.2 1z"/></svg>617-555-0138</span>
  </div>
  <div class="legal">
    Custom homes and interiors rooted in classic New England style, built with care.<br>
    © Vell Architecture &amp; Interiors 1996
  </div>
</footer>

</body>
</html>
```